lawn sign

Lawn Sign
Roofing Gutters Windows

Target Market(s)

roofing

Font styles to use
Sans Serif

Colors
86cfc6
33a6d7
fbee3f
faa54b

Requirements
Must have
• my logo
Nice to have
• designer for now

```html
<!DOCTYPE html>
<html lang="en">
<head>
<meta charset="utf-8">
<title>Harlow Home Exteriors – Lawn Sign</title>
<link rel="stylesheet" href="https://fonts.googleapis.com/css2?family=Cinzel:wght@500&display=swap">
<style>
  :root {
    --backdrop: #e1e1e1;
    --sign-white: #ffffff;
    --band-teal: #86cfc6;
    --band-blue: #33a6d7;
    --headline-yellow: #fbee3f;
    --brand-teal: #1d8b8d;
  }
  html, body {
    margin: 0;
    padding: 0;
    overflow: hidden;
  }
  body {
    width: 1200px;
    height: 800px;
    background: var(--backdrop);
    position: relative;
  }
  .lawn-sign {
    position: absolute;
    left: 138px;
    top: 162px;
    width: 950px;
    height: 480px;
    display: block;
  }
  .brand-name {
    font-family: "Cinzel", serif;
    font-weight: 500;
    fill: var(--brand-teal);
  }
  .headline {
    font-family: "Cinzel", serif;
    font-weight: 500;
    fill: var(--headline-yellow);
  }
</style>
</head>
<body>
  <svg class="lawn-sign" viewBox="0 0 950 480" xmlns="http://www.w3.org/2000/svg" aria-labelledby="sign-title">
    <title id="sign-title">Harlow Home Exteriors – Roofing, Gutters, Windows</title>
    <defs>
      <linearGradient id="band-gradient" x1="0" y1="1" x2="1" y2="0.3">
        <stop offset="0.3" stop-color="var(--band-teal)"/>
        <stop offset="0.72" stop-color="var(--band-blue)"/>
      </linearGradient>
    </defs>

    <rect class="sign-panel" x="0" y="0" width="950" height="480" fill="var(--sign-white)"/>
    <path class="sign-band" d="M0 238 Q475 366 950 238 L950 480 L0 480 Z" fill="url(#band-gradient)"/>

    <g class="brand-lockup">
      <circle class="brand-dot" cx="190" cy="118" r="36" fill="var(--brand-teal)"/>
      <text class="brand-name" x="246" y="131" font-size="36" textLength="520" lengthAdjust="spacingAndGlyphs">Harlow Home Exteriors</text>
    </g>

    <text class="headline" x="30" y="398" font-size="82" textLength="892" lengthAdjust="spacingAndGlyphs">Roofing Gutters Windows</text>
  </svg>
</body>
</html>
```